Toward Bright Morrow (TWBM) Business Card - company with a mission

Note* The file attached... orange with "Toward Bright MORROW" (in CAPS) is our logo. I am also open to having the text "toward bright morrow" OUTSIDE the orange round logo for business card (so yes, you may take the text out).

The info: (the following info are separate. So either you can use Martin or Helena for now, but that will be 2 separate cards, not together in one card. Thanks!!

Martin K Pardo
202.555.0147
martin@towardbrightmorrow.example
Managing Partner

Helena R Voss
202.555.0147
helena@towardbrightmorrow.example
Managing Partner

Our website: www.towardbrightmorrow.example

TWBM LLC stands for Toward Bright Morrow (non profit arm is called dawn lift foundation)—our business is based out of New York City and has a non-profit arm where for every bar of soap you purchase, we donate a bar (don’t want any designs that limits us to only soap). Currently working with South Africa. We want the focus to be organic/natural soap with a mission.

Looking for a clean, fresh design.

Industry/Entity Type

Non-Profit

Requirements
Must have
• Clean, fresh, refreshing. Design should not be too busy.

```html
<!DOCTYPE html>
<html lang="en">
<head>
<meta charset="utf-8">
<title>Toward Bright Morrow — Business Card</title>
<link href="https://fonts.googleapis.com/css2?family=Oswald:wght@300;400;600&display=swap" rel="stylesheet">
<style>
  :root {
    --stage: #ecebe8;
    --card-white: #ffffff;
    --charcoal: #3b3b3c;
    --apricot: #f2aa6a;
    --ink: #2e2e2e;
    --social: #9aa7b4;
  }
  * { box-sizing: border-box; margin: 0; padding: 0; }
  html, body {
    width: 1200px; height: 800px; overflow: hidden;
    background: var(--stage);
    font-family: "Oswald", "Arial Narrow", sans-serif;
  }
  .stage {
    width: 1200px; height: 800px;
    display: flex; align-items: center; justify-content: center; gap: 80px;
  }
  .card {
    position: relative;
    width: 340px; height: 595px;
    overflow: hidden;
    box-shadow: 0 10px 28px rgba(0,0,0,0.18);
  }

  /* Back of card */
  .card--back { background: var(--charcoal); }
  .card--back .brand-disc {
    position: absolute;
    width: 470px; height: 470px;
    left: -20px; top: -170px;
    border-radius: 50%;
    background: var(--apricot);
  }
  .card--back .brand-name {
    position: absolute;
    left: 0; right: 0; top: 95px;
    text-align: center;
    font-weight: 600; font-size: 96px; letter-spacing: 2px; line-height: 1;
    color: var(--charcoal);
  }

  /* Front of card */
  .card--front { background: var(--card-white); }
  .card--front .brand-disc {
    position: absolute;
    width: 205px; height: 205px;
    right: 22px; top: 40px;
    border-radius: 50%;
    background: var(--apricot);
    display: flex; flex-direction: column; align-items: center; justify-content: center;
  }
  .card--front .brand-name {
    font-weight: 600; font-size: 60px; letter-spacing: 1px; line-height: 1;
    color: var(--card-white);
  }
  .card--front .brand-tagline {
    margin-top: 8px;
    font-weight: 600; font-size: 13px; letter-spacing: 1.2px;
    color: var(--card-white);
    text-transform: uppercase;
  }
  .contact {
    position: absolute;
    left: 40px; right: 20px; top: 300px;
    color: var(--ink);
  }
  .contact__name {
    font-weight: 600; font-size: 30px; letter-spacing: 0.5px;
    color: var(--apricot); text-transform: uppercase; line-height: 1.1;
  }
  .contact__role {
    font-weight: 400; font-size: 13px; letter-spacing: 0.5px;
    text-transform: uppercase; margin: 4px 0 18px 2px;
  }
  .contact__line {
    font-weight: 300; font-size: 14px; letter-spacing: 0.3px;
    text-transform: uppercase; line-height: 1.7;
    white-space: nowrap;
  }
  .contact__line--web { font-weight: 400; }
  .social {
    display: flex; gap: 8px; margin-top: 14px;
  }
  .social__tile {
    width: 30px; height: 30px; border-radius: 6px;
    background: var(--social);
  }
</style>
</head>
<body>
  <main class="stage">
    <section class="card card--back" aria-label="Card back">
      <div class="brand-disc"></div>
      <span class="brand-name">TWBM</span>
    </section>

    <section class="card card--front" aria-label="Card front">
      <div class="brand-disc">
        <span class="brand-name">TWBM</span>
        <span class="brand-tagline">Toward Bright Morrow</span>
      </div>
      <div class="contact">
        <p class="contact__name">Helena R Voss</p>
        <p class="contact__role">Managing Partner</p>
        <p class="contact__line">202.555.0147</p>
        <p class="contact__line">helena@towardbrightmorrow.example</p>
        <p class="contact__line contact__line--web">www.towardbrightmorrow.example</p>
        <div class="social" aria-label="Social profiles">
          <span class="social__tile"></span>
          <span class="social__tile"></span>
          <span class="social__tile"></span>
        </div>
      </div>
    </section>
  </main>
</body>
</html>
```